One Page Magazine Ad for New Apartment in Calgary, AB Canada

We need a one page magazine ad for a new apartment community in Calgary, Alberta.

We pride ourselves in providing the highest level of customer service and the best amenities for our community.

COMMUNITY HIGHLIGHTS

- Brand new luxury apartment rental community in the exciting Calgary Beltline neighborhood
- 13 unique spacious floor plans fit for every lifestyle (1BR-1BATH, 2BR-1BATH & 2BR-2BATH)
- Professionally managed
- On-site staff during business hours to help you with any of your needs
- Pet-friendly community
- State of the art Fitness Facility
- 2 rooftop terraces outfitted with 8 Community Brixford BBQs
- Great area for entertaining guests and a safe spot to take your dog out for some fresh air without leaving the building
- 2 resident lounges with multimedia suite, 60-inch TVs, Zentra Duo, Silver Pin Arcade system, Poker table
- Great venues to host your next party, open 24/7 free to use and bookable by residents for free!
- Monthly resident events and parties hosted by the on-site staff
- Underground secured guest and resident parking available
- Electric Car Charging Stations
- Garbage & Recycling chutes on every floor
- Controlled Access/Building
- Gated Underground Parking Garage
- Adjacent to the Beltline neighborhood bike lane on 12th Avenue SW
- Elevators - Underground Secured Bike Storage and bike repair workstation
- On-site Maintenance
- Box Waiting Package Management System
- Additional Storage Available
- Footsteps away from the local Valemart Grocery and Valemart Wine Store
- Minutes away from the new free leash dog park Ridgewell Park

APARTMENT AMENITIES

- Gourmet Kitchen with 4 piece Stainless Steel Appliances (Stove, Fridge, Microwave and Dishwasher)
- In suite dryer and washer
- Large Closets
- Patio/Balcony
- City and mountain views
- Ceramic Tile and Laminate Hardwood Flooring
- Quartz Counter-tops
- Roller Blinds for all Windows
- Walk-in Closets

For branding style, floor plans, amenities and photos please visit our website www.stayatthefenwick.example

Target Market(s)

Young Adults and Recently Single Market

Industry/Entity Type

Real Estate

Font styles to use
Sans Serif

Colors
f37122

Requirements
Must have
• - Pictures of the community
• - Possibly use of a stock photo

```html
<!DOCTYPE html>
<html lang="en">
<head>
<meta charset="utf-8">
<title>The Fenwick – Enjoy the Life of Luxury</title>
<link href="https://fonts.googleapis.com/css2?family=PT+Sans:wght@400;700&family=Montserrat:wght@400;500&display=swap" rel="stylesheet">
<style>
  :root {
    --orange: #f37122;
    --orange-deep: #e8601a;
    --ink: #2b211b;
    --white: #ffffff;
    --grey-label: #d9d9d9;
    --grey-footer: #bdbdbd;
    --logo-bg: #f1f1f1;
    --logo-ink: #5b5b5b;
  }
  * { box-sizing: border-box; margin: 0; padding: 0; }
  html, body { width: 927px; height: 1200px; overflow: hidden; background: var(--white); }
  body { font-family: "PT Sans", Arial, sans-serif; color: var(--ink); }
  .ad { position: relative; width: 927px; height: 1200px; overflow: hidden; background: var(--white); }

  .photo { position: absolute; }
  .hero-photo { left: 0; top: 0; width: 690px; height: 614px;
    background: linear-gradient(160deg, #c9c4bb 0%, #8e8375 35%, #5d5249 62%, #b7a999 100%); }

  .brand { position: absolute; left: 690px; top: 0; width: 237px; height: 156px; background: var(--logo-bg);
    display: flex; align-items: center; justify-content: center; gap: 12px; }
  .brand-mark { width: 14px; height: 14px; background: var(--logo-ink); }
  .brand-name { font-family: "Montserrat", sans-serif; font-weight: 400; font-size: 24px; letter-spacing: 4px; color: var(--logo-ink); }

  .side-panel { position: absolute; left: 690px; top: 156px; width: 237px; height: 458px; background: var(--orange); }
  .side-photo { left: 694px; width: 233px; }
  .terrace-photo { top: 168px; height: 143px; background: linear-gradient(180deg, #b8c3cc 0%, #8a8078 60%, #d8d2c9 100%); }
  .building-photo { top: 316px; height: 145px; background: linear-gradient(180deg, #7f98b6 0%, #9a5b49 55%, #cfc7bd 100%); }
  .lounge-photo { top: 466px; height: 148px; background: linear-gradient(170deg, #e4e2df 0%, #9ea6ab 50%, #3b4148 100%); }

  .headline-band { position: absolute; left: 45px; top: 524px; width: 645px; height: 90px;
    background: rgba(232, 96, 26, 0.82); display: flex; align-items: center; padding-left: 52px; }
  .headline { font-family: "PT Sans", Arial, sans-serif; font-weight: 700; font-size: 47px; color: var(--white); letter-spacing: -1px; }

  .section-label { position: absolute; font-weight: 700; font-size: 16px; color: var(--ink); letter-spacing: 0.2px; }
  .amenities-label { left: 27px; top: 636px; width: 253px; height: 36px; background: var(--grey-label); padding: 9px 0 0 16px; }

  .amenities-list { position: absolute; left: 34px; top: 683px; width: 330px; list-style: none; font-size: 14.6px; line-height: 17.2px; }
  .amenities-list li { padding-left: 10px; text-indent: -10px; }
  .amenities-list li::before { content: "- "; }

  .theater-photo { left: 26px; top: 890px; width: 326px; height: 211px;
    background: linear-gradient(180deg, #4a4d52 0%, #2b2d31 55%, #15161a 100%); }

  .site-note { position: absolute; left: 0; top: 1110px; width: 371px; height: 90px; background: var(--grey-footer);
    text-align: center; padding-top: 10px; }
  .site-note p { font-size: 13.6px; line-height: 16px; font-weight: 700; color: var(--ink); }
  .site-note .url { font-size: 18px; margin-top: 6px; }

  .highlights-panel { position: absolute; left: 371px; top: 614px; width: 556px; height: 586px; background: var(--orange); }
  .highlights-label { left: 386px; top: 632px; width: 212px; height: 30px; background: var(--white); padding: 6px 0 0 17px; font-size: 15.5px; }
  .highlights-list { position: absolute; left: 396px; top: 676px; width: 518px; list-style: none; font-size: 13.3px; line-height: 16.2px; letter-spacing: -0.1px; }
  .highlights-list li { padding-left: 10px; text-indent: -10px; }
  .highlights-list li::before { content: "- "; }
</style>
</head>
<body>
<main class="ad">
  <div class="photo hero-photo" role="img" aria-label="Photo of a bright modern apartment with a stainless steel kitchen, bar stools and a grey sofa with patterned cushions"></div>

  <div class="brand">
    <span class="brand-mark"></span>
    <span class="brand-name">THE FENWICK</span>
  </div>

  <div class="side-panel"></div>
  <div class="photo side-photo terrace-photo" role="img" aria-label="Photo of the rooftop terrace with a giant outdoor chess set"></div>
  <div class="photo side-photo building-photo" role="img" aria-label="Photo of the apartment building exterior at street level"></div>
  <div class="photo side-photo lounge-photo" role="img" aria-label="Photo of the resident lounge with a poker table and colourful chairs"></div>

  <div class="headline-band"><h1 class="headline">ENJOY THE LIFE OF LUXURY</h1></div>

  <h2 class="section-label amenities-label">APARTMENT AMENITIES</h2>
  <ul class="amenities-list">
    <li>Gourmet Kitchen with 4 piece Stainless Steel Appliances (Stove, Fridge, Microwave and Dishwasher)</li>
    <li>In suite dryer and washer</li>
    <li>Large Closets</li>
    <li>Patio/Balcony</li>
    <li>City and mountain views</li>
    <li>Ceramic Tile and Laminate Hardwood Flooring</li>
    <li>Quartz Counter-tops</li>
    <li>Roller Blinds for all Windows</li>
    <li>Walk-in Closets</li>
  </ul>

  <div class="photo theater-photo" role="img" aria-label="Photo of the resident multimedia theatre room with rows of dark leather seats"></div>

  <div class="site-note">
    <p>For branding style, floor plans, amenities<br>and photos please visit our website</p>
    <p class="url">www.stayatthefenwick.example</p>
  </div>

  <section class="highlights-panel"></section>
  <h2 class="section-label highlights-label">COMMUNITY HIGHLIGHTS</h2>
  <ul class="highlights-list">
    <li>Brand new luxury apartment rental community in the exciting Calgary Beltline neighborhood</li>
    <li>13 unique spacious floor plans fit for every lifestyle (1BR-1BATH, 2BR-1BATH &amp; 2BR-2BATH)</li>
    <li>Professionally managed</li>
    <li>On-site staff during business hours to help you with any of your needs</li>
    <li>Pet-friendly community</li>
    <li>State of the art Fitness Facility</li>
    <li>2 rooftop terraces outfitted with 8 Community Brixford BBQs</li>
    <li>Great area for entertaining guests and a safe spot to take your dog out for some fresh air without leaving the building</li>
    <li>2 resident lounges with multimedia suite, 60-inch TVs, Zentra Duo, Silver Pin Arcade system, Poker table</li>
    <li>Great venues to host your next party, open 24/7 free to use and bookable by residents for free!</li>
    <li>Monthly resident events and parties hosted by the on-site staff</li>
    <li>Underground secured guest and resident parking available</li>
    <li>Electric Car Charging Stations</li>
    <li>Garbage &amp; Recycling chutes on every floor</li>
    <li>Controlled Access/Building</li>
    <li>Gated Underground Parking Garage</li>
    <li>Adjacent to the Beltline neighborhood bike lane on 12th Avenue SW</li>
    <li>Elevators - Underground Secured Bike Storage and bike repair workstation</li>
    <li>On-site Maintenance</li>
    <li>Box Waiting Package Management System</li>
    <li>Additional Storage Available</li>
    <li>Footsteps away from the local Valemart Grocery and Valemart Wine Store</li>
    <li>Minutes away from the new free leash dog park Ridgewell Park</li>
  </ul>
</main>
</body>
</html>
```